Design clean technology service-based company website

Hello, We are looking to reskin our company website. We are an environmental inspection company and test for Asbestos, Lead and Mold along with other contaminants. People depend on the results to be accurate and fast. We are regulated by the plain badge and State regulations. We work a lot with business to business and business to customer. We are wanting to make our new presentation to be modern and easy for customers to interact with us, understand our process and services while providing valuable environmental informational resource and updates. We are a technology based company and will be providing instantaneous results as reports come in for the customers. We are needing good calls to action on the site to direct them to setup a new inspection. Each user will have a backend access to their job information with invoices, reports, status, etc. We have developed software to be able to proved these reports and want to look the part.

My current website is www.trypelmarix.com

Helllo we are wanting to make sure we have good time to select the right website for us and also have the additional time to select other pages of the website. We have received great designs and have consolidated our requests into a document for the next set of iterations.

Target Market(s)

Home Owners, Contractors, Engineers, Real Estate Agents, Building Owners, Insurance Adjusters

Industry/Entity Type

Environmental Consultant

Number of Pages Required

5+ page

Font styles to use
Sans Serif

Colors
0355a3
9bcb3c
7f7f7f
f5f5f5
000000

Requirements
Must have
• Use our existing logo to design around
• The layouts look good in mobile mode for understanding and selecting services and signing up
• Clean Modern Layout
• Have all pages on the website have a similar layout and feel
• Clearly communicate services along with bundle service packages
• Detail the customer journey with graphic design
• Great call to actions to either schedule inspection online, call, text, chat
Nice to have
• Have an interactive graphic for where to test for lead, asbestos and mold.
• I like the barney kolts top order line bar - see attached
• Have clear question and answer page layouts for asbestos, lead and mold
• Show Company reviews
• Have clear Resources pages for all types of contaminants
Should not have
• My current website is www.trypelmarix.com

```html
<!DOCTYPE html>
<html lang="en">
<head>
<meta charset="utf-8">
<title>Pelmarix Environmental Inspections</title>
<link href="https://fonts.googleapis.com/css2?family=Roboto:wght@300;400;500;700&display=swap" rel="stylesheet">
<style>
:root{
  --green:#4cb81c;
  --ink:#333333;
  --text:#6b6b6b;
  --grey-bg:#ebebeb;
  --footer:#5f5f61;
  --footer-dark:#3d3d3f;
  --white:#ffffff;
  --line:#d5d5d5;
}
*{box-sizing:border-box;margin:0;padding:0}
html,body{width:1200px;height:3766px;overflow:hidden}
body{position:relative;font-family:'Roboto',Arial,sans-serif;color:var(--ink);background:var(--white)}
.abs{position:absolute}
.hl{color:var(--green)}

.topbar{left:0;top:0;width:1200px;height:50px;z-index:3}
.topbar .mail{left:690px;top:12px;font-size:16px;color:#555;display:flex;align-items:center;gap:8px}
.topbar .call{left:910px;top:0;width:212px;height:50px;background:var(--green);color:#fff;border-radius:0 0 6px 6px;font-size:22px;display:flex;align-items:center;justify-content:center;gap:10px}
.header{left:0;top:50px;width:1200px;height:100px;background:rgba(255,255,255,.92);z-index:2}
.logo{left:78px;top:20px;display:flex;align-items:center;gap:12px;font-size:46px;font-weight:500;color:var(--ink)}
.logo .dot{width:22px;height:22px;border-radius:50%;background:var(--green)}
.nav{right:70px;top:28px;display:flex;gap:2px}
.nav a{font-size:17px;color:#444;text-decoration:none;padding:12px 12px;border-radius:4px;text-transform:uppercase}
.nav a.active{background:var(--green);color:#fff}

.hero{left:0;top:0;width:1200px;height:720px;background:linear-gradient(100deg,#3a3a38 0%,#6d6c66 40%,#b4b0a6 65%,#d8d3c6 85%,#9d9a90 100%)}
.hero-copy{left:78px;top:335px;color:#fff}
.hero-copy h1{font-size:33px;font-weight:500;line-height:45px;letter-spacing:.5px}
.hero-copy p{font-size:22px;margin-top:14px}
.hero-btns{display:flex;gap:14px;margin-top:18px}
.btn{font-size:18px;padding:12px 14px;color:#fff;font-weight:500}
.btn.outline{border:2px solid #fff}
.btn.solid{background:var(--green);font-weight:700;padding:14px 24px}

.intro-title{left:0;top:766px;width:1200px;text-align:center;font-size:42px;font-weight:500;color:#555}
.intro-lead{left:220px;top:836px;width:760px;text-align:center;font-size:15px;line-height:22px;color:var(--text)}
.col{font-size:15px;line-height:23px;color:var(--text)}
.col h3{font-size:28px;font-weight:500;color:#444;margin-bottom:14px}

.owner-band{left:0;top:1376px;width:1200px;height:230px;background:var(--green)}
.owner-card{left:311px;top:1135px;width:625px;height:392px;background:#fff;box-shadow:0 8px 14px rgba(0,0,0,.25)}
.owner-card h2{position:absolute;top:38px;width:100%;text-align:center;font-size:42px;font-weight:500;color:#555}
.owner-photo{left:246px;top:1248px;width:156px;height:158px;background:linear-gradient(160deg,#7fa35a,#4b5f6d 60%,#2f3a48)}
.owner-text{left:443px;top:1278px;width:460px}
.owner-text h4{font-size:22px;font-weight:400;color:#444;margin-bottom:14px}
.owner-text p{font-size:15px;line-height:23px;color:var(--text)}

.services{left:0;top:1606px;width:1200px;height:854px;background:var(--grey-bg)}
.sec-title{left:0;width:1200px;text-align:center;font-size:42px;font-weight:500;color:#555}
.card{background:#f2f2f2;border:1px solid var(--line)}
.card h4{font-size:22px;font-weight:400;color:#444;margin-bottom:12px}
.card p{font-size:15px;line-height:23px;color:var(--text)}
.ph{position:absolute}

.blog-card{width:467px;height:226px;background:#fff;border:1px solid var(--line)}
.blog-card .body{position:absolute;top:26px;width:225px}
.blog-card h5{font-size:19px;font-weight:700;color:#333;line-height:25px;margin-bottom:10px}
.blog-card p{font-size:15px;line-height:22px;color:var(--text)}
.date{width:66px;height:78px;background:var(--green);color:#fff;text-align:center;font-size:30px;padding-top:8px;line-height:32px}
.date span{display:block;font-size:15px;line-height:20px}

.testi{left:0;top:2886px;width:1200px;height:528px;background:var(--green)}
.t-card{top:3030px;width:324px;height:188px;background:#fff;border-radius:6px;box-shadow:0 6px 10px rgba(0,0,0,.25);text-align:center;padding:56px 26px 0}
.t-card p{font-size:15px;line-height:23px;color:#555}
.t-card .who{color:var(--green);font-size:17px;margin-top:10px}
.quote{top:2998px;width:66px;height:66px;border-radius:50%;background:#555;border:5px solid #fff;display:flex;align-items:center;justify-content:center}
.badge{top:3288px;height:76px;background:rgba(255,255,255,.9)}

.footer{left:0;top:3414px;width:1200px;height:301px;background:var(--footer)}
.f-logo{left:78px;top:3500px;font-size:46px;font-weight:500;color:#fff}
.socials{left:103px;top:3592px;display:flex;gap:14px}
.socials span{width:40px;height:40px;border:2px solid #fff;border-radius:50%}
.f-head{font-size:24px;color:var(--green);font-weight:500}
.f-line{display:flex;gap:14px;align-items:flex-start;font-size:16px;line-height:22px;color:#f0f0f0}
.copy{left:0;top:3715px;width:1200px;height:51px;background:var(--footer-dark);color:#ddd;font-size:15px;text-align:center;line-height:51px}
.copy b{color:var(--green)}
</style>
</head>
<body>

<div class="abs hero" role="img" aria-label="Worker in protective suit spraying a corrugated asbestos roof"></div>

<div class="abs topbar">
  <div class="abs mail">
    <svg width="16" height="12" viewBox="0 0 16 12"><rect x="0.5" y="0.5" width="15" height="11" fill="#555"/><path d="M1 1l7 6 7-6" stroke="#fff" fill="none"/></svg>
    info@trypelmarix.com
  </div>
  <div class="abs call">
    <svg width="20" height="20" viewBox="0 0 24 24"><path d="M6.6 10.8c1.4 2.8 3.8 5.1 6.6 6.6l2.2-2.2c.3-.3.7-.4 1-.2 1.1.4 2.3.6 3.6.6.6 0 1 .4 1 1V20c0 .6-.4 1-1 1C10.6 21 3 13.4 3 4c0-.6.4-1 1-1h3.5c.6 0 1 .4 1 1 0 1.3.2 2.5.6 3.6.1.3 0 .7-.2 1z" fill="#fff"/></svg>
    303-555-0148
  </div>
</div>

<header class="abs header">
  <div class="abs logo">Pelmarix<span class="dot"></span></div>
  <nav class="abs nav">
    <a class="active">Home</a><a>Our Services</a><a>Resources</a><a>Blog</a><a>Q &amp; A</a><a>Reviews</a><a>Connect</a>
  </nav>
</header>

<div class="abs hero-copy">
  <h1>FAST, DEPENDABLE RESULT WHEN<br>IT METTERS THE MOST</h1>
  <p>24/7/365 SAME DAY SERVICE</p>
  <div class="hero-btns"><span class="btn outline">CONTACT NOW</span><span class="btn solid">KNOW MORE</span></div>
</div>

<h2 class="abs intro-title"><span class="hl">Environmental</span> Testing Evolved</h2>
<p class="abs intro-lead">Pelmarix grew up in the rough and tumble disaster restoration industry. Time and time again, we saw projects small and large brought to a stand-still to await environmental testing and results.</p>
<div class="abs col" style="left:80px;top:902px;width:530px">
  <p>First, we had to know when it's prudent or even required by law to test for asbestos, lead-based paint, mold or other contaminants. Then we had to track down reliable testing companies, facilities or equipment. Next, we had to ensure we safeguarded people and property in the process of obtaining test samples. Finally, we had to wait, sometimes days or even weeks, while property owners languished and spent more and more money on expensive temporary living or working space.</p>
</div>
<div class="abs col" style="left:630px;top:902px;width:490px">
  <h3>The Next Step</h3>
  <p>At Pelmarix, we are experienced in assessing the environmental hazards that merit or even require testing by law. We are trained and certified to safely obtain environmental test samples. And we have established a working relationship with top-rated testing facilities that enable us to get most test results within hours, not days.</p>
</div>

<div class="abs owner-band"></div>
<div class="abs owner-card"><h2>Owner</h2></div>
<div class="abs owner-photo" role="img" aria-label="Portrait photo of the owner"></div>
<div class="abs owner-text">
  <h4>Dean Harlow</h4>
  <p>In his experience with inspecting property and mitigating environmental issues, Dean saw one project after another brought to a standstill awaiting testing results. He believed property owners should be able to get test results in hours, not days. Pelmarix was born.</p>
</div>

<section class="abs services"></section>
<h2 class="abs sec-title" style="top:1655px"><span class="hl">Our</span> Services</h2>

<div class="abs card" style="left:78px;top:1752px;width:665px;height:290px">
  <div class="ph" role="img" aria-label="Technician in protective suit sampling for asbestos" style="left:0;top:0;width:333px;height:288px;background:linear-gradient(135deg,#5a5f63,#9ea3a6 50%,#3d4245)"></div>
  <div style="position:absolute;left:355px;top:80px;width:285px"><h4>Asbestos Testing</h4><p>Start your project off right and test for asbestos FIRST. When starting any construction project where you will be disturbing building materials, you should always check for asbestos.</p></div>
</div>
<div class="abs card" style="left:78px;top:2096px;width:665px;height:290px">
  <div style="position:absolute;left:22px;top:90px;width:285px"><h4>Mold Testing</h4><p>Mold stinks. It's unsightly and, if unchecked, can cost thousands of dollars to eradicate and clean up. But that's not the worst of it.</p></div>
  <div class="ph" role="img" aria-label="Mold growth on a wall" style="left:331px;top:0;width:333px;height:288px;background:radial-gradient(circle at 55% 55%,#8a7f66,#d9d4c6 55%,#eeeae2)"></div>
</div>
<div class="abs card" style="left:790px;top:1752px;width:332px;height:634px">
  <div class="ph" role="img" aria-label="Peeling teal lead-based paint on a window sill" style="left:0;top:0;width:330px;height:318px;background:linear-gradient(160deg,#3f6d70,#7fb6b4 55%,#2b4a4c)"></div>
  <div style="position:absolute;left:22px;top:410px;width:290px"><h4>Lead Based Paint Testing</h4><p>So before you start that renovation or demolition on your property, we'll help you make sure you know what you're dealing with and that you take every necessary step to protect the people.</p></div>
</div>

<h2 class="abs sec-title" style="top:2508px"><span class="hl">Latest</span> Blog</h2>
<div class="abs blog-card" style="left:98px;top:2580px">
  <div class="ph" role="img" aria-label="Technician in protective suit at a work site" style="left:0;top:0;width:208px;height:224px;background:linear-gradient(135deg,#5a5f63,#a7abad 50%,#3d4245)"></div>
  <div class="abs date" style="left:142px;top:52px">29<span>APR</span></div>
  <div class="body" style="left:228px"><h5>Lorem Ipsum is simply dummy text.</h5><p>Lorem Ipsum is simply dummy text of the printing and typesetting industry. Lorem Ipsum has been the industry's standard dummy text.</p></div>
</div>
<div class="abs blog-card" style="left:632px;top:2580px">
  <div class="ph" role="img" aria-label="Crew removing roof material outdoors" style="left:0;top:0;width:208px;height:224px;background:linear-gradient(160deg,#5d7a4a,#8e8a78 50%,#6b5a42)"></div>
  <div class="abs date" style="left:142px;top:136px">29<span>APR</span></div>
  <div class="body" style="left:228px"><h5>Lorem Ipsum is simply dummy text.</h5><p>Lorem Ipsum is simply dummy text of the printing and typesetting industry. Lorem Ipsum has been the industry's standard dummy text.</p></div>
</div>

<section class="abs testi"></section>
<h2 class="abs sec-title" style="top:2926px;color:#fff">Testimonials</h2>
<div class="abs t-card" style="left:78px"><p>Lorem Ipsum is simply dummy text of the printing and typesetting industry. Lorem Ipsum has been the industry.</p><div class="who">- Client Name</div></div>
<div class="abs t-card" style="left:439px"><p>Lorem Ipsum is simply dummy text of the printing and typesetting industry. Lorem Ipsum has been the industry.</p><div class="who">- Client Name</div></div>
<div class="abs t-card" style="left:798px"><p>Lorem Ipsum is simply dummy text of the printing and typesetting industry. Lorem Ipsum has been the industry.</p><div class="who">- Client Name</div></div>
<div class="abs quote" style="left:207px"><svg width="26" height="20" viewBox="0 0 26 20"><path d="M0 20V11C0 4 4 0 10 0v4c-3 0-5 2-5 6h5v10zM14 20V11c0-7 4-11 10-11v4c-3 0-5 2-5 6h5v10z" fill="#fff"/></svg></div>
<div class="abs quote" style="left:567px"><svg width="26" height="20" viewBox="0 0 26 20"><path d="M0 20V11C0 4 4 0 10 0v4c-3 0-5 2-5 6h5v10zM14 20V11c0-7 4-11 10-11v4c-3 0-5 2-5 6h5v10z" fill="#fff"/></svg></div>
<div class="abs quote" style="left:927px"><svg width="26" height="20" viewBox="0 0 26 20"><path d="M0 20V11C0 4 4 0 10 0v4c-3 0-5 2-5 6h5v10zM14 20V11c0-7 4-11 10-11v4c-3 0-5 2-5 6h5v10z" fill="#fff"/></svg></div>

<div class="abs badge" style="left:78px;width:200px;border-radius:38px"></div>
<div class="abs badge" style="left:292px;width:190px;border-radius:6px"></div>
<div class="abs badge" style="left:552px;width:100px;border-radius:50%;height:100px;top:3276px"></div>
<div class="abs badge" style="left:722px;width:186px;border-radius:8px"></div>
<div class="abs badge" style="left:934px;width:170px;border-radius:6px"></div>

<footer class="abs footer"></footer>
<div class="abs f-logo">Pelmarix</div>
<div class="abs socials"><span></span><span></span><span></span><span></span><span></span></div>
<div class="abs f-head" style="left:440px;top:3468px">Contact Info</div>
<div class="abs" style="left:440px;top:3520px;display:flex;flex-direction:column;gap:18px">
  <div class="f-line"><svg width="18" height="22" viewBox="0 0 18 22"><path d="M9 1a7 7 0 0 0-7 7c0 5 7 13 7 13s7-8 7-13a7 7 0 0 0-7-7z" fill="none" stroke="#4cb81c" stroke-width="2"/><circle cx="9" cy="8" r="2.5" fill="#4cb81c"/></svg><span>4720 S. Meadowline Ave. Ste. 210<br>Denver, Co. 80219</span></div>
  <div class="f-line"><svg width="18" height="18" viewBox="0 0 24 24"><path d="M6.6 10.8c1.4 2.8 3.8 5.1 6.6 6.6l2.2-2.2c.3-.3.7-.4 1-.2 1.1.4 2.3.6 3.6.6.6 0 1 .4 1 1V20c0 .6-.4 1-1 1C10.6 21 3 13.4 3 4c0-.6.4-1 1-1h3.5c.6 0 1 .4 1 1 0 1.3.2 2.5.6 3.6.1.3 0 .7-.2 1z" fill="none" stroke="#4cb81c" stroke-width="2"/></svg><span>303-555-0148</span></div>
  <div class="f-line"><svg width="18" height="14" viewBox="0 0 18 14"><rect x="1" y="1" width="16" height="12" fill="none" stroke="#4cb81c" stroke-width="2"/><path d="M1 1l8 7 8-7" fill="none" stroke="#4cb81c" stroke-width="2"/></svg><span>info at trypelmarix.com</span></div>
</div>
<div class="abs f-head" style="left:802px;top:3468px">Watch videos</div>
<div class="abs" role="img" aria-label="Video thumbnail of an inspection" style="left:802px;top:3522px;width:218px;height:136px;background:linear-gradient(135deg,#3a3a3a,#8a5a3a 55%,#4a3328)"></div>
<svg class="abs" style="left:885px;top:3564px" width="52" height="52" viewBox="0 0 52 52"><circle cx="26" cy="26" r="24" fill="rgba(0,0,0,.5)" stroke="#fff" stroke-width="3"/><path d="M21 16l15 10-15 10z" fill="#fff"/></svg>
<div class="abs copy"><b>©Pelmarix</b> - 2017. All Rights Reserved.</div>

</body>
</html>
```